Stationery and Business Card Design

We need stationary design for our new company larkvale. Larkvale is a company that provides city apartment rentals for tourists in Athens We need business cards, letterheads for A4 and A5 and envelopes for A4 A5. The design needs to be modern, friendly and corporate.

Target Market(s)

City Tourists

Industry/Entity Type

Tourism

```html
<!DOCTYPE html>
<html lang="en">
<head>
<meta charset="utf-8">
<title>Larkvale Business Card</title>
<link href="https://fonts.googleapis.com/css2?family=Raleway:wght@400;500&display=swap" rel="stylesheet">
<style>
  :root {
    --brand: #8a1a4e;
    --paper: #ececee;
    --ink: #333338;
    --backdrop: #d3d3d3;
    --white: #ffffff;
  }
  * { margin: 0; padding: 0; box-sizing: border-box; }
  html, body {
    width: 1200px;
    height: 754px;
    overflow: hidden;
    background: var(--backdrop);
    font-family: "Raleway", sans-serif;
  }
  .stage {
    position: relative;
    width: 1200px;
    height: 754px;
  }
  .card {
    position: absolute;
    top: 242px;
    width: 458px;
    height: 255px;
  }
  .card--front {
    left: 120px;
    background: var(--paper);
    border-top: 8px solid var(--brand);
  }
  .card--back {
    left: 624px;
    background: var(--brand);
  }
  .brand {
    position: absolute;
    left: 0;
    width: 100%;
    display: flex;
    flex-direction: column;
    align-items: center;
  }
  .card--front .brand { top: 56px; }
  .card--back .brand { top: 77px; }
  .brand__square {
    width: 54px;
    height: 54px;
  }
  .card--front .brand__square { background: var(--brand); }
  .card--back .brand__square { background: var(--white); }
  .brand__name {
    margin-top: 4px;
    font-size: 37px;
    font-weight: 400;
    line-height: 1.1;
    letter-spacing: -0.5px;
  }
  .card--front .brand__name { color: var(--brand); }
  .card--back .brand__name { color: var(--white); }
  .contact {
    position: absolute;
    left: 0;
    bottom: 18px;
    width: 100%;
    text-align: center;
    font-size: 11px;
    font-weight: 400;
    font-style: normal;
    line-height: 14px;
    color: var(--ink);
  }
  .contact__label { color: var(--brand); font-weight: 500; }
</style>
</head>
<body>
  <main class="stage">
    <section class="card card--front">
      <div class="brand">
        <div class="brand__square"></div>
        <div class="brand__name">Larkvale</div>
      </div>
      <address class="contact">
        <div>22 Lykavittou St, Kolonaki, Athens 106 72</div>
        <div><span class="contact__label">T:</span> +30 210 555 0142 · <span class="contact__label">F:</span> +30 210 555 0178 · www.larkvale.com</div>
      </address>
    </section>
    <section class="card card--back">
      <div class="brand">
        <div class="brand__square"></div>
        <div class="brand__name">Larkvale</div>
      </div>
    </section>
  </main>
</body>
</html>
```